VantoMedix website

I have a plumfield hosting website already & have been using wordpress.
See www.vantomedix-sample.com
I have a logo's already.
I need a front page "VantoMedix". I have 3 products: (need separate pages)
1) the "GlideTray" (can't supply images ATM)
2) the "TubeKeeper" (several stills below & animation: http://www.clipvault-example.com/watch?v=Z7HqR20mW3x&list=QPtr8B_kzoepWnXcM4Lq5B_T&feature=share)
3) the "FastPart" animation here: http://clipv.example/pwrtk-Mmo_E & logo as below

It needs to be corporate & professional looking. VantoMedix is an innovative design house for medical devices.

Reason: Hi Designers, thanks for all your work to date - there have been some great designs. We'll be providing feedback to some of you in the near future. The reason we have extended the deadline is simply that we are too busy with other aspects of the business to focus on this at the moment. Kind regards, the VantoMedix team.

Dear Designers,

VantoMedix apologies for the delay due to our busyness. 
Please help us to understand the process here:
are we getting fully working websites? With multiple pages? Will we be able to modify them?
If not, what is the output?

Kind regards,
the Vanto team.

```html
<!DOCTYPE html>
<html lang="en">
<head>
<meta charset="utf-8">
<title>TubeKeeper IV – VantoMedix</title>
<link href="https://fonts.googleapis.com/css2?family=Lato:wght@400;700&display=swap" rel="stylesheet">
<style>
  :root{
    --blue:#2a9fd8;
    --navy:#1f3f7a;
    --orange:#f47a20;
    --dark:#2d2d2d;
    --text:#333;
    --band:#eef1f6;
    --bar:#ede9e6;
    --white:#fff;
  }
  *{box-sizing:border-box;margin:0;padding:0}
  html,body{width:858px;height:1200px;overflow:hidden}
  body{position:relative;background:var(--white);font-family:"Lato",Arial,sans-serif;color:var(--text)}
  .abs{position:absolute}

  .topbar{left:0;top:0;width:858px;height:24px;background:var(--dark)}
  .phone{left:132px;top:3px;color:#eee;font-size:15px;display:flex;align-items:center;gap:6px}
  .social{left:668px;top:5px;display:flex;gap:3px}
  .social span{width:14px;height:14px;border-radius:2px;display:block}

  .header{left:0;top:24px;width:858px;height:66px;background:var(--white)}
  .brand{left:120px;top:42px;font-size:23px;font-weight:700;color:var(--blue);letter-spacing:-.3px}
  .nav{right:121px;top:49px;display:flex;gap:19px;font-size:9.5px;color:#222}
  .nav .active{position:relative}
  .nav .active::after{content:"";position:absolute;left:-3px;right:-3px;bottom:-6px;height:2px;background:var(--orange)}

  .hero{left:0;top:90px;width:858px;height:202px;background:radial-gradient(ellipse at center,#fff 55%,#eef5fb 100%)}
  .product-title{left:129px;top:117px;font-weight:700;font-size:32px;letter-spacing:.5px;color:var(--navy);line-height:1}
  .page-heading{left:130px;top:154px;font-size:18px;color:var(--orange)}
  .hero-desc{left:130px;top:187px;width:270px;font-size:10.5px;line-height:1.35;color:#444}
  .btn{top:230px;height:38px;width:127px;color:#fff;font-size:14px;display:flex;align-items:center;justify-content:center;letter-spacing:.3px}
  .btn-order{left:132px;background:var(--blue)}
  .btn-contact{left:264px;background:var(--navy)}
  .video{left:415px;top:98px;width:313px;height:184px;border:1px solid #e2d9d2;background:linear-gradient(135deg,#d7d2e6 0%,#c9c5dc 45%,#e9d6c8 100%)}
  .play{left:119px;top:64px;width:76px;height:46px;background:#f2f2f2;border:1px solid #ccc}

  h2{font-weight:400;font-size:15px;color:var(--blue)}
  .body-text{font-size:7.4px;line-height:1.38;color:#333}
  .body-text p+p{margin-top:9px}

  .figure{background:#fff;border:1px solid #ddd;border-radius:3px;overflow:hidden;box-shadow:0 1px 3px rgba(0,0,0,.12)}
  .figure .shot{width:100%;height:calc(100% - 20px)}
  .figure .caption{height:20px;background:var(--orange);color:#fff;font-size:7px;font-weight:700;display:flex;align-items:center;justify-content:center}

  .how-band{left:0;top:464px;width:858px;height:160px;background:var(--band)}

  .faq{left:120px;width:616px}
  .faq-item{height:24px;background:var(--bar);border-radius:2px;display:flex;align-items:center;justify-content:space-between;padding:0 8px;font-size:9.5px;color:#333;margin-bottom:5px}
  .faq-item .ico{width:10px;height:10px;border-radius:50%;background:#555;color:#fff;font-size:9px;line-height:10px;text-align:center}
  .faq-answer{font-size:7.4px;line-height:1.38;margin:8px 0 10px}

  .gallery-img{top:898px;width:148px;height:114px;background:#fff;border:1px solid #ddd;box-shadow:0 1px 3px rgba(0,0,0,.15);padding:4px}
  .gallery-img div{width:100%;height:100%}
  .arrow{top:950px}

  .testimonial{left:185px;top:1061px;width:345px;font-size:7.6px;line-height:1.35}
  .testimonial .sign{margin-top:9px;font-size:6.5px;font-style:italic;font-weight:700;line-height:1.4}
  .avatar{left:125px;top:1061px;width:51px;height:55px;background:linear-gradient(#d9c4b4,#b89a86);border:2px solid #ddd}
  .field{left:541px;width:154px;height:18px;border:1px solid #bbb;border-radius:3px;background:#fff;font-size:7px;font-style:italic;color:#333;padding:4px 5px}
  .send{left:700px;top:1063px;width:36px;height:38px;background:var(--orange);color:#fff;font-size:10px;display:flex;align-items:center;justify-content:center}

  .footer{left:0;top:1138px;width:858px;height:62px;background:#2b2b2b}
  .foot-links{left:0;top:1155px;width:858px;text-align:center;font-size:8px;color:var(--blue)}
  .foot-links span.sep{color:#ccc;margin:0 9px}
  .copyright{left:0;top:1175px;width:858px;text-align:center;font-size:7px;color:#eee}
</style>
</head>
<body>

<div class="abs topbar"></div>
<div class="abs phone">
  <svg width="14" height="14" viewBox="0 0 24 24" fill="none" stroke="#ddd" stroke-width="2"><path d="M5 3h4l2 5-3 2a12 12 0 0 0 6 6l2-3 5 2v4a2 2 0 0 1-2 2A17 17 0 0 1 3 5a2 2 0 0 1 2-2z"/></svg>
  555-014-2386
</div>
<div class="abs social" aria-label="Social links">
  <span style="background:#3b5b99"></span><span style="background:#d9452f"></span><span style="background:#3aa0d8"></span>
</div>

<header class="abs header"></header>
<div class="abs brand">vantomedix</div>
<nav class="abs nav">
  <span>Home</span><span>About Us</span><span>GlideTray</span><span class="active">TubeKeeper</span><span>FastPart</span><span>Ask a Question</span><span>Contact VantoMedix</span>
</nav>

<section class="abs hero"></section>
<h1 class="abs product-title">TUBEKEEPER IV</h1>
<div class="abs page-heading">Page Heading</div>
<p class="abs hero-desc">A short description of the device you can put here. Lorem Ipsum is a dummy text and this device is real.</p>
<div class="abs btn btn-order">ORDER NOW</div>
<div class="abs btn btn-contact">CONTACT US</div>
<div class="abs video" role="img" aria-label="Product animation video of the device fitted on a patient's arm">
  <div class="abs play">
    <svg width="76" height="46"><circle cx="38" cy="23" r="13" fill="#999"/><path d="M34 16l11 7-11 7z" fill="#fff"/></svg>
  </div>
</div>

<h2 class="abs" style="left:121px;top:314px">About Device</h2>
<div class="abs body-text" style="left:121px;top:341px;width:404px">
  <p>Sed ut perspiciatis unde omnis iste natus error sit voluptatem accusantium doloremque laudantium, totam rem aperiam, eaque ipsa quae ab illo inventore veritatis et quasi architecto beatae vitae dicta sunt explicabo. Nemo enim ipsam voluptatem quia voluptas sit aspernatur aut odit aut fugit, sed quia consequuntur magni dolores eos qui ratione voluptatem sequi nesciunt.</p>
  <p>Sed ut perspiciatis unde omnis iste natus error sit voluptatem accusantium doloremque laudantium, totam rem aperiam, eaque ipsa quae ab illo inventore veritatis et quasi architecto beatae vitae dicta sunt explicabo.</p>
</div>
<figure class="abs figure" style="left:556px;top:316px;width:180px;height:135px">
  <div class="shot" role="img" aria-label="Illustration of the device being wrapped around an arm and fixed with velcro" style="background:linear-gradient(160deg,#f4f4f8,#c9c6e6)"></div>
  <figcaption class="caption">Device is being wrapped around and fixed with velcro</figcaption>
</figure>

<section class="abs how-band"></section>
<figure class="abs figure" style="left:120px;top:478px;width:180px;height:134px">
  <div class="shot" role="img" aria-label="Illustration of the device limiting hand rotation" style="background:linear-gradient(180deg,#f6f6fa,#c8c4e8)"></div>
  <figcaption class="caption">Device is providing movement limitation to pronation</figcaption>
</figure>
<h2 class="abs" style="left:332px;top:473px">How It Works</h2>
<div class="abs body-text" style="left:332px;top:501px;width:404px">
  <p>Sed ut perspiciatis unde omnis iste natus error sit voluptatem accusantium doloremque laudantium, totam rem aperiam, eaque ipsa quae ab illo inventore veritatis et quasi architecto beatae vitae dicta sunt explicabo. Nemo enim ipsam voluptatem quia voluptas sit aspernatur aut odit aut fugit, sed quia consequuntur magni dolores eos qui ratione voluptatem sequi nesciunt.</p>
  <p>Sed ut perspiciatis unde omnis iste natus error sit voluptatem accusantium doloremque laudantium, totam rem aperiam, eaque ipsa quae ab illo inventore veritatis et quasi architecto beatae vitae dicta sunt explicabo.</p>
</div>

<section class="abs faq" style="top:636px">
  <div class="faq-item"><span>How many hours should I use it?</span><span class="ico">−</span></div>
  <p class="faq-answer">Sed ut perspiciatis unde omnis iste natus error sit voluptatem accusantium doloremque laudantium, totam rem aperiam, eaque ipsa quae ab illo inventore veritatis et quasi architecto beatae vitae dicta sunt explicabo. Nemo enim ipsam voluptatem quia voluptas sit aspernatur aut odit aut fugit, sed quia consequuntur magni dolores eos qui ratione voluptatem sequi nesciunt.</p>
  <div class="faq-item"><span>What it cost me?</span><span class="ico">+</span></div>
  <div class="faq-item"><span>How it helps?</span><span class="ico">+</span></div>
  <div class="faq-item"><span>Where should I buy?</span><span class="ico">+</span></div>
  <div class="faq-item"><span>Is it mechanical or automatic?</span><span class="ico">+</span></div>
  <div class="faq-item"><span>For what kind of injury it suits?</span><span class="ico">+</span></div>
</section>

<h2 class="abs" style="left:119px;top:866px">Image Gallery</h2>
<svg class="abs arrow" style="left:149px" width="12" height="18" viewBox="0 0 12 18"><path d="M10 2L3 9l7 7" fill="none" stroke="var(--blue)" stroke-width="3"/></svg>
<div class="abs gallery-img" style="left:200px"><div role="img" aria-label="Device rendering, top view" style="background:linear-gradient(160deg,#f3efe8,#c7c3e6)"></div></div>
<div class="abs gallery-img" style="left:356px"><div role="img" aria-label="Device rendering, close-up of strap" style="background:linear-gradient(160deg,#e9e6ee,#b9b4da)"></div></div>
<div class="abs gallery-img" style="left:512px"><div role="img" aria-label="Device rendering with hand, side view" style="background:linear-gradient(160deg,#f4f4f6,#cfcbe8)"></div></div>
<svg class="abs arrow" style="left:692px" width="12" height="18" viewBox="0 0 12 18"><path d="M2 2l7 7-7 7" fill="none" stroke="var(--blue)" stroke-width="3"/></svg>

<h2 class="abs" style="left:121px;top:1035px">Happy Customers</h2>
<div class="abs avatar" role="img" aria-label="Customer portrait"></div>
<div class="abs testimonial">
  <p>Nullam eros mi, mollis in sollicitudin non, tincidunt sed enim. Sed et felis metus, rhoncus ornare nibh. Ut at magna leo. Suspendisse egestas est ac dolor imperdiet pretium. Lorem ipsum dolor sit amet, consectetur adipiscing elit.</p>
  <p class="sign">Marlene, Australia<br>Thank you Vantomedix</p>
</div>

<h2 class="abs" style="left:539px;top:1035px">Feedback &amp; Enquiry</h2>
<div class="abs field" style="top:1063px">Your name</div>
<div class="abs field" style="top:1084px">Email</div>
<div class="abs send">SEND</div>

<footer class="abs footer"></footer>
<div class="abs foot-links">
  Home<span class="sep">/</span>About Us<span class="sep">/</span>GlideTray<span class="sep">/</span>TubeKeeper<span class="sep">/</span>FastPart<span class="sep">/</span>Ask a Question<span class="sep">/</span>Contact VantoMedix
</div>
<div class="abs copyright">Copyright 2006 - 2013 © VantoMedix - All Rights Reserved - Business Inquiries | Feedback | Privacy | Tell a Friend</div>

</body>
</html>
```